nutrition ebook cover

i need a cover for a ebook designed, the book is called Amber Lattice so i would like that somewhere on the cover. i would also like the word nutrition followed by my company logo that i have attached below somewhere on the cover( i have attached two logos and would like to see with both separatley), i would like this to be faded into the background if possible, perhaps in a upper or lower corner. i would also like to see options with and without the picture i have attached below. the look I'm going for is professional and clean. this is a fat loss, healthy eating booklet. the winning designer i would like to design the following pages within the book aswell no more than 10 pages, that i will provide all content for, i just need help with putting what i have on pdf in a way that looks professional and cool. this would ideally covered in the rate that is paid for the cover. i also have other booklets i need made so the winning designer will most likely get that work too at a later date for an additional fee of course.

Industry/Entity Type

Nutrition

Requirements
Nice to have
• Outside images are welcomed, happy to purchase any stock images used from a outside source

```html
<!DOCTYPE html>
<html lang="en">
<head>
<meta charset="utf-8">
<title>Amber Lattice – ebook cover options</title>
<link href="https://fonts.googleapis.com/css2?family=League+Spartan:wght@600;700&display=swap" rel="stylesheet">
<style>
  :root {
    --board-grey: #b3b3b3;
    --page-white: #ffffff;
    --leaf-light: #63b146;
    --leaf-dark: #4b9641;
    --rule-green: #8cc63f;
    --tomato-red: #cd1e27;
    --slate-deep: #1c2e33;
    --slate-mid: #2f4a4e;
    --herb-green: #3f7a3a;
    --brand-white: #ffffff;
  }
  * { box-sizing: border-box; margin: 0; padding: 0; }
  html, body {
    width: 1200px; height: 890px; overflow: hidden;
    background: var(--board-grey);
    font-family: "League Spartan", "Helvetica Neue", Arial, sans-serif;
  }
  .board { position: relative; width: 1200px; height: 890px; }
  .cover {
    position: absolute; top: 44px; width: 535px; height: 802px;
    background: var(--page-white);
    display: flex; flex-direction: column;
  }
  .cover--badge { left: 49px; }
  .cover--plain { left: 616px; }

  .produce {
    height: 180px; flex: none;
    background:
      radial-gradient(ellipse 30% 45% at 25% 40%, rgba(214,170,80,.45), transparent 70%),
      radial-gradient(ellipse 40% 35% at 70% 30%, rgba(110,170,80,.55), transparent 70%),
      linear-gradient(120deg, var(--slate-mid), var(--slate-deep));
  }
  .produce--bottom {
    height: 177px;
    background:
      radial-gradient(ellipse 35% 60% at 38% 55%, rgba(88,150,70,.75), transparent 70%),
      radial-gradient(ellipse 20% 30% at 18% 20%, rgba(200,110,60,.5), transparent 70%),
      linear-gradient(100deg, var(--slate-mid), var(--slate-deep));
    position: relative;
  }
  .rule { height: 3px; flex: none; background: var(--rule-green); }

  .title-panel {
    flex: 1;
    display: flex; flex-direction: column; align-items: center; justify-content: center;
    padding-top: 12px;
  }
  .title-main {
    font-weight: 700; font-size: 132px; line-height: .9; letter-spacing: -2px;
    background: linear-gradient(172deg, var(--leaf-light) 0 50%, var(--leaf-dark) 50% 100%);
    -webkit-background-clip: text; background-clip: text; color: transparent;
  }
  .title-sub {
    font-weight: 700; font-size: 96px; line-height: 1; letter-spacing: -2px;
    color: var(--tomato-red); margin-top: 14px;
  }

  .brand {
    position: absolute; right: 24px; bottom: 40px;
    display: flex; align-items: center; gap: 8px;
    color: var(--brand-white); font-weight: 600; font-size: 22px;
  }
  .brand-mark {
    width: 72px; height: 72px; border-radius: 50%;
    border: 2px solid rgba(255,255,255,.55);
    background: rgba(20,30,34,.55);
  }
  .cover--plain .brand { bottom: 30px; }
</style>
</head>
<body>
<main class="board">
  <article class="cover cover--badge">
    <div class="produce" role="img" aria-label="Photo of fresh vegetables on a dark slate table: leek, potatoes, mushrooms, tomato, peppercorns and rocket"></div>
    <div class="rule"></div>
    <section class="title-panel">
      <h1 class="title-main">Amber</h1>
      <p class="title-sub">Lattice</p>
    </section>
    <div class="rule"></div>
    <div class="produce produce--bottom" role="img" aria-label="Photo of broccoli, cherry tomatoes, rocket and a pepper mill on a dark slate table">
      <div class="brand"><span>Nutrition Kestrel</span><span class="brand-mark"></span></div>
    </div>
  </article>

  <article class="cover cover--plain">
    <div class="produce" role="img" aria-label="Photo of fresh vegetables on a dark slate table: leek, potatoes, mushrooms, tomato, peppercorns and rocket"></div>
    <div class="rule"></div>
    <section class="title-panel">
      <h1 class="title-main">Amber</h1>
      <p class="title-sub">Lattice</p>
    </section>
    <div class="rule"></div>
    <div class="produce produce--bottom" role="img" aria-label="Photo of broccoli, cherry tomatoes, rocket and a pepper mill on a dark slate table">
      <div class="brand"><span>Nutrition Kestrel</span></div>
    </div>
  </article>
</main>
</body>
</html>
```